Presentation Folder Design for Photographer

Professional photographer requires a presentation folder for marketing.
I specialise in architecture, corporate & commercial photography. The folder will be used to promote my architectural photography services to real estate, accomodation & architect clients.

I'm looking for a modern clean design that complements my logo with complimentary text & colours. I want to use some images in the design, probably a mix of images not just architectural. I need a print ready design in PDF as well as a PSD file that I can possibly edit / update images later on.

The folder will be a double sided design with no need for pockets included in the design. Overall dimensions are 430mm ( folded down the centre ) x 315mm with a 5mm trim & bleed.

The layout would be as follows :

Front cover - Logo + maybe some images or some other design work.

Inside front cover - Some text about my services.

ARCHITECTURE
Commercial Residential Real Estate Drone Floorpans Accommodation

CORPORATE
Studio Headshots Environmental Portraits Staff Photography

COMMERCIAL
Product Advertising Fashion Event Stock

Inside back cover - no text as a seperate price list will sit here.

Outside back cover - I was thinking of having a collage of images worked into
the design but open to the designers input as well.
I also have another logo with phone number & web address
I would like on the back cover - Will be included in the files
provided.

I have a black background & white background version of my logo I will include both for the design work. I'm trying to get away from an all black design so if using the black logo I don't want a completely black page design, just becomes to heavy.

I'm redoing my website soon so please base the folder design around my logo text & colours not my current website as it's very outdated.

Logo brand guide is as follows

Main Font Font: Reislust
Main Font Color: #fff
Slogan Font Font: Ubuntu Bold
Monogram Font Font: Venti Medium
Container Color: #fff

Please respect the copyright on the images provided and delete all content once the design has been completed.
Thanks.

```html
<!DOCTYPE html>
<html lang="en">
<head>
<meta charset="utf-8">
<title>Clear Aperture – Presentation Folder</title>
<link href="https://fonts.googleapis.com/css2?family=Lato:wght@400;700&family=Montserrat:wght@400&display=swap" rel="stylesheet">
<style>
  :root {
    --backdrop: #e2e0e1;
    --ink: #111111;
    --band: #1a1a1a;
    --band-dark: #141414;
    --gold: #c39a4c;
    --gold-deep: #b07a2a;
    --paper: #ffffff;
    --label: #3a3a3a;
    --gap: #f4f4f4;
  }
  * { margin: 0; padding: 0; box-sizing: border-box; }
  html, body { width: 979px; height: 1200px; overflow: hidden; }
  body { background: var(--backdrop); position: relative; font-family: "Lato", sans-serif; }

  .spread { position: absolute; left: 134px; width: 720px; box-shadow: 0 2px 8px rgba(0,0,0,.25); overflow: hidden; }
  .spread--outside { top: 75px; height: 483px; background: var(--gap); }
  .spread--inside { top: 636px; height: 484px; background: var(--paper); }

  .spread-label { position: absolute; left: 0; width: 979px; text-align: center; font-family: "Montserrat", sans-serif; font-size: 25px; letter-spacing: 1px; color: var(--label); }
  .spread-label--outside { top: 576px; }
  .spread-label--inside { top: 1139px; }

  /* outside */
  .header-band { position: absolute; left: 0; top: 0; width: 720px; height: 133px; background: var(--band); }
  .header-band::after { content: ""; position: absolute; left: 360px; top: 0; width: 360px; height: 100%; background: var(--band-dark); }
  .footer-band { position: absolute; left: 0; top: 443px; width: 720px; height: 40px; background: var(--band); }
  .footer-band::after { content: ""; position: absolute; left: 360px; top: 0; width: 360px; height: 100%; background: var(--band-dark); }

  .brand { position: absolute; display: flex; align-items: center; z-index: 2; font-family: "Montserrat", sans-serif; font-weight: 400; color: #ffffff; text-transform: uppercase; white-space: nowrap; }
  .brand-dot { border: 2px solid var(--gold); border-radius: 50%; }
  .brand--back { left: 86px; top: 57px; font-size: 9px; letter-spacing: 2px; gap: 7px; }
  .brand--back .brand-dot { width: 14px; height: 14px; }
  .brand--front { left: 452px; top: 53px; font-size: 15px; letter-spacing: 3.5px; gap: 10px; }
  .brand--front .brand-dot { width: 22px; height: 22px; }

  .contact { position: absolute; display: flex; align-items: center; gap: 6px; color: var(--gold); z-index: 2; white-space: nowrap; }
  .contact svg { fill: none; stroke: #dddddd; stroke-width: 1.4; }
  .contact--web { font-family: "Lato", sans-serif; font-size: 10px; letter-spacing: .3px; }
  .contact--phone { font-family: "Montserrat", sans-serif; font-size: 13px; letter-spacing: 3px; }
  .footer-band .contact--web { left: 89px; top: 13px; }
  .footer-band .contact--phone { left: 486px; top: 12px; }

  .photo { position: absolute; }
  .photo--portrait { left: 0; top: 137px; width: 138px; height: 152px; background: radial-gradient(circle at 55% 45%, #c9a98c 0%, #7a5a66 35%, #2c1a30 75%); }
  .photo--coast { left: 140px; top: 137px; width: 131px; height: 152px; background: linear-gradient(180deg, #e09a3a 0%, #8a4a22 40%, #6a6a66 65%, #a77a48 100%); }
  .photo--garage { left: 0; top: 292px; width: 272px; height: 149px; background: linear-gradient(180deg, #d89a88 0%, #c9a272 35%, #8a6a40 65%, #5a3a1e 100%); }
  .photo--garden { left: 275px; top: 137px; width: 162px; height: 304px; background: linear-gradient(180deg, #6a7a3a 0%, #c8c4b8 35%, #e8e8ee 65%, #8a9a5a 100%); }
  .photo--garden::after { content: ""; position: absolute; left: 85px; top: 0; width: 77px; height: 100%; background: rgba(0,0,0,.12); }
  .photo--bedroom { left: 439px; top: 137px; width: 282px; height: 148px; background: linear-gradient(180deg, #d8d2c8 0%, #ece8e2 55%, #a88a6a 100%); }
  .photo--stars { left: 439px; top: 288px; width: 132px; height: 153px; background: linear-gradient(180deg, #1a3ab8 0%, #2a5ad8 55%, #3a6aa8 80%, #2a4a6a 100%); }
  .photo--stage { left: 574px; top: 288px; width: 147px; height: 153px; background: radial-gradient(ellipse at 45% 55%, #d8281e 0%, #8a1a12 40%, #1a0c10 85%); }

  /* inside */
  .fold-shade { position: absolute; left: 360px; top: 0; width: 120px; height: 484px; background: linear-gradient(90deg, #ececec 0%, #f6f6f6 40%, rgba(255,255,255,0) 100%); }
  .services { position: absolute; left: 28px; top: 40px; width: 320px; }
  .service { margin-bottom: 38px; }
  .service-title { font-size: 15px; font-weight: 400; color: var(--gold-deep); line-height: 20px; letter-spacing: .2px; }
  .service-list { font-size: 14px; color: var(--ink); line-height: 20px; letter-spacing: -.1px; }

  .pocket { position: absolute; left: 0; top: 0; width: 720px; height: 484px; }
  .pocket path { fill: #000000; }
  .spread--inside .contact--phone { left: 98px; top: 381px; }
  .spread--inside .contact--web { left: 98px; top: 407px; }
  .brand--pocket { left: 464px; top: 394px; font-size: 15px; letter-spacing: 3.5px; gap: 10px; color: var(--gold); }
  .brand--pocket .brand-dot { width: 22px; height: 22px; }
</style>
</head>
<body>

<section class="spread spread--outside" aria-label="Folder outside">
  <div class="header-band">
    <div class="brand brand--back"><span class="brand-dot"></span>Clear Aperture</div>
    <div class="brand brand--front"><span class="brand-dot"></span>Clear Aperture</div>
  </div>

  <div class="photo photo--portrait" role="img" aria-label="Fine art portrait with silver jewellery on a dark purple background"></div>
  <div class="photo photo--coast" role="img" aria-label="Rocky coastline at sunset with misty surf"></div>
  <div class="photo photo--garage" role="img" aria-label="Blue vintage car in front of an old service station at dusk"></div>
  <div class="photo photo--garden" role="img" aria-label="Fashion shoot in a garden with wisteria and a white dress"></div>
  <div class="photo photo--bedroom" role="img" aria-label="Bright bedroom interior with framed prints"></div>
  <div class="photo photo--stars" role="img" aria-label="Star trails over a sea stack on the coast"></div>
  <div class="photo photo--stage" role="img" aria-label="Performer in a red coat on stage"></div>

  <div class="footer-band">
    <div class="contact contact--web">
      <svg width="11" height="11" viewBox="0 0 12 12" aria-hidden="true"><circle cx="6" cy="6" r="5"/><ellipse cx="6" cy="6" rx="2.2" ry="5"/><line x1="1" y1="6" x2="11" y2="6"/></svg>
      www.clearaperture.com.au
    </div>
    <div class="contact contact--phone">
      <svg width="10" height="10" viewBox="0 0 12 12" aria-hidden="true"><path d="M2 1.5 L4 1.5 L5 4 L3.8 5 Q5 7.5 7 8.2 L8 7 L10.5 8 L10.5 10 Q6 11 3.5 8 Q1 5 2 1.5 Z"/></svg>
      0400 555 019
    </div>
  </div>
</section>
<div class="spread-label spread-label--outside">Outside</div>

<section class="spread spread--inside" aria-label="Folder inside">
  <div class="fold-shade"></div>
  <div class="services">
    <div class="service">
      <h2 class="service-title">ARCHITECTURE</h2>
      <p class="service-list">Commercial Residential Real Estate Drone Floorpans Accommodation</p>
    </div>
    <div class="service">
      <h2 class="service-title">CORPORATE</h2>
      <p class="service-list">Studio Headshots Environmental Portraits Staff Photography</p>
    </div>
    <div class="service">
      <h2 class="service-title">COMMERCIAL</h2>
      <p class="service-list">Product Advertising Fashion Event Stock</p>
    </div>
  </div>

  <svg class="pocket" viewBox="0 0 720 484" aria-hidden="true">
    <path d="M0 333 H318 Q338 333 341 352 L360 484 H0 Z"/>
    <path d="M720 332 H402 Q382 332 379 351 L360 484 H720 Z"/>
  </svg>
  <div class="contact contact--phone">
    <svg width="10" height="10" viewBox="0 0 12 12" aria-hidden="true"><path d="M2 1.5 L4 1.5 L5 4 L3.8 5 Q5 7.5 7 8.2 L8 7 L10.5 8 L10.5 10 Q6 11 3.5 8 Q1 5 2 1.5 Z"/></svg>
    0400 555 019
  </div>
  <div class="contact contact--web">
    <svg width="11" height="11" viewBox="0 0 12 12" aria-hidden="true"><circle cx="6" cy="6" r="5"/><ellipse cx="6" cy="6" rx="2.2" ry="5"/><line x1="1" y1="6" x2="11" y2="6"/></svg>
    www.clearaperture.com.au
  </div>
  <div class="brand brand--pocket"><span class="brand-dot"></span>Clear Aperture</div>
</section>
<div class="spread-label spread-label--inside">inside</div>

</body>
</html>
```